I need to launch a new website that more accurately reflects what we do as a business. We are an IT Reseller that specialises in delivering innovative solutions covering supply, implementation and support. My current website is www.vornetikx.com and was something I designed myself on the Hub Nimbo website. This was fine for the first 2 years but now I need something more professional and detailed. A couple of websites for companies similar to Brindle KTR are www.quarvolen.co.uk and www.ferrimund.co.uk. By looking at these it will hopefully give you an idea as to what I am trying to achieve.

Target Market(s)

UK based companies with between 30-250 employees, no fixed vertical

Coding

Coded - Design and coding required

Number of Pages Required

4 page

Font styles to use
Sans Serif

Colors
33a6d7
0592cd
85cae6

Requirements
Must have
• Contact details page to include a "Get in touch with us " section, About Us page, IT Support page to include the headings 1/ Proactive Monitoring 2/ 24 x 7 Support 3/ Security and Data Back-up 4/ Built-in Compliance (GDPR) 5/ Responsive IT Support. I am happy to provide the wording for these headings.
Clean crisp home screen with a Menu offering the requested drop down options.
Nice to have
• Easy to navigate site with a good flow. I have updated a page regarding cloud services, this would be great to have as a separate drop down menu option. I would like to have different Cloud logo's in ideally the Brindle Blue colour. Can you please add the photograph of Thornwick Lodge which is my office in the contact us page.
Should not have
• I definitely DO NOT want a photo/view of London on the home page!!

```html
<!DOCTYPE html>
<html lang="en">
<head>
<meta charset="utf-8">
<title>Brindle KTR – IT Reseller</title>
<link href="https://fonts.googleapis.com/css2?family=Montserrat:wght@400;500;600;700&display=swap" rel="stylesheet">
<style>
:root{
  --brand:#0a30e2;
  --ink:#111111;
  --text:#333333;
  --muted:#7a7a7a;
  --soft-bg:#eef6fd;
  --dark:#1f1f1f;
  --white:#ffffff;
  --line:#d4d4d4;
}
*{box-sizing:border-box;margin:0;padding:0}
html,body{width:1200px;height:2720px;overflow:hidden}
body{position:relative;font-family:'Montserrat',sans-serif;color:var(--text);background:var(--white)}
.abs{position:absolute}
.btn{display:flex;align-items:center;justify-content:center;background:var(--brand);color:var(--white);font-weight:500;text-decoration:none}

/* header */
.site-header{top:0;left:0;width:1200px;height:87px;background:var(--white)}
.brand{left:66px;top:26px;display:flex;align-items:center;gap:12px;font-size:20px;font-weight:500;color:var(--ink)}
.brand-dot{width:40px;height:40px;border-radius:50%;background:var(--brand)}
.main-nav{left:315px;top:35px;display:flex;gap:21px;font-size:14px;font-weight:500;color:var(--ink)}
.quote-btn{left:831px;top:29px;width:173px;height:33px;font-size:15px}

/* hero */
.hero{top:87px;left:0;width:1200px;height:483px;overflow:hidden}
.hero-photo{inset:0;background:linear-gradient(100deg,#d9dce0 0%,#c5cbd3 40%,#6d7f99 65%,#1f3150 100%)}
.hero-kicker{left:67px;top:92px;font-size:29px;font-weight:600;color:var(--ink)}
.hero-title{left:66px;top:128px;font-size:44px;font-weight:700;color:var(--brand)}
.hero-sub{left:67px;top:182px;font-size:24px;font-weight:700;color:var(--brand);letter-spacing:.3px}
.hero-copy{left:67px;top:240px;width:475px;font-size:14px;line-height:23px;color:var(--ink)}
.hero-cta{left:66px;top:340px;width:183px;height:38px;font-size:16px}
.audit-card{left:765px;top:58px;width:304px;height:364px;background:var(--white);border-radius:4px;padding:18px 20px}
.audit-card h2{font-size:20px;font-weight:500;color:var(--ink);text-align:center;margin-bottom:20px}
.audit-card p{font-size:10.5px;line-height:16px;color:#444;margin-bottom:18px}
.field-label{font-size:10.5px;color:#555;margin-bottom:4px;display:block}
.field{height:28px;border:1px solid var(--line);margin-bottom:20px;background:var(--white)}
.name-row{display:flex;gap:6px}
.name-row>div{flex:1}
.audit-btn{width:264px;height:37px;font-size:13px;font-weight:600;margin-top:-2px}

/* service */
.dots-deco{left:1070px;top:568px;width:130px;height:136px;background:radial-gradient(circle at 70% 45%,rgba(10,48,226,.75) 0%,rgba(10,48,226,.35) 40%,rgba(10,48,226,0) 70%)}
.team-photo{left:12px;top:707px;width:574px;height:317px;background:linear-gradient(180deg,#f3f3f3,#d8d8d8 55%,#f6f6f6);border-radius:4px}
.service-title{left:641px;top:748px;font-size:34px;line-height:35px;font-weight:700;color:var(--brand)}
.service-copy{left:641px;top:844px;width:520px;font-size:19.5px;line-height:33.5px;color:var(--ink)}
.service-btn{left:641px;top:967px;width:140px;height:38px;font-size:16px}

/* about */
.about{top:1111px;left:0;width:1200px;height:542px;background:var(--soft-bg)}
.section-title{width:1200px;left:0;text-align:center;font-weight:600}
.about-title{top:36px;font-size:42px;color:var(--brand)}
.rule{height:3px;background:var(--brand)}
.about-card{top:207px;width:313px;height:270px;background:var(--white);border-radius:4px;box-shadow:0 2px 10px rgba(0,0,0,.06);text-align:center;padding:80px 22px 0}
.about-card h3{font-size:22px;font-weight:500;color:var(--ink);margin-bottom:14px}
.about-card p{font-size:12px;line-height:21.3px;color:var(--ink)}
.icon-disc{top:146px;width:95px;height:95px;border-radius:50%;background:var(--brand);display:flex;align-items:center;justify-content:center}

/* testimonials */
.testimonials{top:1653px;left:0;width:1200px;height:556px}
.test-title{top:60px;font-size:40px;font-weight:700;color:var(--ink)}
.test-sub{top:137px;left:0;width:1200px;text-align:center;font-size:15px;color:var(--muted)}
.quote-card{top:206px;width:287px;height:259px;background:var(--white);box-shadow:0 2px 12px rgba(0,0,0,.08);text-align:center}
.quote-tag{left:23px;top:-18px;width:53px;height:44px;background:var(--brand);display:flex;align-items:center;justify-content:center}
.avatar{left:104px;top:19px;width:79px;height:79px;border-radius:50%;background:linear-gradient(160deg,#6d6d6d,#2d2d2d)}
.quote-text{left:22px;top:117px;width:243px;font-size:9px;line-height:13px;color:var(--muted)}
.quote-name{left:0;top:203px;width:287px;font-size:15px;font-weight:600;color:var(--ink)}
.quote-role{left:0;top:224px;width:287px;font-size:15px;font-weight:500;color:var(--brand)}

/* subscribe */
.subscribe{top:2209px;left:0;width:1200px;height:215px;background:var(--dark)}
.subscribe h2{position:absolute;top:53px;width:1200px;text-align:center;font-size:18px;font-weight:700;color:var(--white)}
.sub-input{left:365px;top:109px;width:342px;height:48px;background:var(--white);font-size:12px;color:#c2c2c2;padding:0 22px;display:flex;align-items:center}
.sub-btn{left:707px;top:109px;width:127px;height:48px;background:#0757e0;font-size:18px;font-weight:700}

/* footer */
.footer-head{font-size:15px;font-weight:600;color:var(--ink)}
.footer-text{font-size:12.5px;color:var(--ink);line-height:15px}
.footer-link{font-size:12px;color:var(--ink)}
.contact-line{display:flex;align-items:center;gap:8px;font-size:12.5px;font-weight:600;color:var(--ink)}
.footer-contact-btn{left:775px;top:2513px;width:220px;height:43px;background:var(--dark);color:var(--white);font-size:18px;font-weight:500}
.follow-box{left:775px;top:2583px;width:220px;height:43px;border:1.5px solid var(--dark);display:flex;align-items:center;padding-left:21px;gap:16px;font-size:14px;font-weight:600;color:var(--ink)}
.social{width:11px;height:11px;background:var(--ink);border-radius:2px}
.copyright{top:2683px;left:0;width:1200px;height:37px;background:var(--dark);color:var(--white);font-size:16px;display:flex;align-items:center;justify-content:center}
</style>
</head>
<body>

<header class="site-header abs">
  <div class="brand abs"><span class="brand-dot"></span>Brindle KTR</div>
  <nav class="main-nav abs"><span>About Us</span><span>Contact Us</span><span>IT Support Page</span></nav>
  <a class="quote-btn btn abs">Get Free Quote</a>
</header>

<section class="hero abs">
  <div class="hero-photo abs" role="img" aria-label="Photo of an IT support engineer with headset working at monitors"></div>
  <div class="hero-kicker abs">WE ARE AN IT RESELLER</div>
  <h1 class="hero-title abs">THAT SPECIALISES IN</h1>
  <div class="hero-sub abs">DELIVERING INNOVATIVE SOLUTIONS</div>
  <p class="hero-copy abs">Lorem Ipsum is simply dummy text of the printing and typesetting industry. Lorem Ipsum has been the industry's standard dummy text ever since the 1500s,</p>
  <a class="hero-cta btn abs">Contact Us Now</a>
  <form class="audit-card abs">
    <h2>Free IT Discovery Audit</h2>
    <p>Book a free, no-obligation discovery audit to see how your IT really is performing.</p>
    <div class="name-row">
      <div><span class="field-label">First Name*</span><div class="field"></div></div>
      <div><span class="field-label">Last Name*</span><div class="field"></div></div>
    </div>
    <span class="field-label">Email*</span><div class="field"></div>
    <span class="field-label">Phone*</span><div class="field"></div>
    <div class="audit-btn btn">SOLVE YOUR IT ISSUES</div>
  </form>
</section>

<div class="dots-deco abs" role="img" aria-label="Decorative blue dot cluster"></div>

<section class="service">
  <div class="team-photo abs" role="img" aria-label="Photo of a business team meeting around a table"></div>
  <h2 class="service-title abs">A NEW AND PERSONALISED<br>LEVEL OF SERVICE</h2>
  <p class="service-copy abs">Find out what it is like to have a customised service tailored to your business requirements today and for the future.</p>
  <a class="service-btn btn abs">Read More</a>
</section>

<section class="about abs">
  <h2 class="section-title about-title abs">About Us</h2>
  <div class="rule abs" style="left:530px;top:85px;width:94px"></div>
  <div class="rule abs" style="left:630px;top:85px;width:56px"></div>

  <div class="icon-disc abs" style="left:205px">
    <svg width="54" height="54" viewBox="0 0 54 54" fill="none" stroke="#fff" stroke-width="2"><circle cx="27" cy="16" r="7"/><circle cx="17" cy="27" r="5"/><circle cx="37" cy="27" r="5"/><path d="M6 30 L14 44 L22 44 M48 30 L40 44 L32 44"/></svg>
  </div>
  <div class="about-card abs" style="left:96px">
    <h3>Our Experience</h3>
    <p>With a wealth of knowledge within the IT Service delivery industry we are confident that we can become the trusted adviser and partner to you and your business. With a personal and tailored solution that will grow and develop along with your business.</p>
  </div>

  <div class="icon-disc abs" style="left:552px">
    <svg width="56" height="54" viewBox="0 0 56 54" fill="none" stroke="#fff" stroke-width="2"><rect x="6" y="8" width="44" height="30"/><path d="M4 40 H52 M28 40 V50 M20 50 L28 42 L36 50 M12 16 L18 22 M30 14 L38 26"/><circle cx="22" cy="30" r="2"/></svg>
  </div>
  <div class="about-card abs" style="left:448px">
    <h3>Our Approach</h3>
    <p>We understand that no two businesses are the same so why should the service delivered be any different. We aim to understand all your business drivers so we can not only add a world class services but be there to advise you every step of the way.</p>
  </div>

  <div class="icon-disc abs" style="left:913px">
    <svg width="56" height="54" viewBox="0 0 56 54" fill="none" stroke="#fff" stroke-width="2"><circle cx="22" cy="22" r="9"/><path d="M8 48 C8 36 36 36 36 48 Z"/><path d="M34 10 H52 V24 H42 L38 28 V24 H34 Z"/></svg>
  </div>
  <div class="about-card abs" style="left:805px">
    <h3>Why Us?</h3>
    <p>Our experience and consultative approach will allow us to give you honest advice. We aim to give you a vendor neutral, technology led view into our ever changing market. By sticking to these principles we will only offer something that is right for you.</p>
  </div>
</section>

<section class="testimonials abs">
  <h2 class="section-title test-title abs">Our Testimonials</h2>
  <div class="rule abs" style="left:451px;top:120px;width:180px"></div>
  <div class="rule abs" style="left:645px;top:120px;width:105px"></div>
  <p class="test-sub abs">Lorem Ipsum is simply dummy text of the printing and typesetting industry.</p>

  <article class="quote-card abs" style="left:135px">
    <div class="quote-tag abs"><svg width="26" height="22" viewBox="0 0 26 22" fill="#fff"><circle cx="6" cy="7" r="5"/><path d="M10 8 Q10 18 3 20 L3 17 Q7 15 7 10 Z"/><circle cx="19" cy="7" r="5"/><path d="M23 8 Q23 18 16 20 L16 17 Q20 15 20 10 Z"/></svg></div>
    <div class="avatar abs" role="img" aria-label="Portrait of client"></div>
    <p class="quote-text abs">Lorem Ipsum is simply dummy text of the printing and typesetting industry. Lorem Ipsum has been the industry's standard dummy text ever since the 1500s, when an unknown</p>
    <div class="quote-name abs">John doe</div>
    <div class="quote-role abs">Business Man</div>
  </article>

  <article class="quote-card abs" style="left:456px">
    <div class="quote-tag abs"><svg width="26" height="22" viewBox="0 0 26 22" fill="#fff"><circle cx="6" cy="7" r="5"/><path d="M10 8 Q10 18 3 20 L3 17 Q7 15 7 10 Z"/><circle cx="19" cy="7" r="5"/><path d="M23 8 Q23 18 16 20 L16 17 Q20 15 20 10 Z"/></svg></div>
    <div class="avatar abs" role="img" aria-label="Portrait of client"></div>
    <p class="quote-text abs">Lorem Ipsum is simply dummy text of the printing and typesetting industry. Lorem Ipsum has been the industry's standard dummy text ever since the 1500s, when an unknown</p>
    <div class="quote-name abs">John doe</div>
    <div class="quote-role abs">Legal Lawyer</div>
  </article>

  <article class="quote-card abs" style="left:776px">
    <div class="quote-tag abs"><svg width="26" height="22" viewBox="0 0 26 22" fill="#fff"><circle cx="6" cy="7" r="5"/><path d="M10 8 Q10 18 3 20 L3 17 Q7 15 7 10 Z"/><circle cx="19" cy="7" r="5"/><path d="M23 8 Q23 18 16 20 L16 17 Q20 15 20 10 Z"/></svg></div>
    <div class="avatar abs" role="img" aria-label="Portrait of client"></div>
    <p class="quote-text abs">Lorem Ipsum is simply dummy text of the printing and typesetting industry. Lorem Ipsum has been the industry's standard dummy text ever since the 1500s, when an unknown</p>
    <div class="quote-name abs">John doe</div>
    <div class="quote-role abs">Web Developer</div>
  </article>
</section>

<section class="subscribe abs">
  <h2>Subscribe and get best IT service</h2>
  <div class="sub-input abs">Examplel@business.com</div>
  <a class="sub-btn btn abs">Subscribe</a>
</section>

<footer>
  <div class="footer-head abs" style="left:206px;top:2486px">CONTACTS</div>
  <p class="footer-text abs" style="left:206px;top:2527px">14 Alder Row,<br>Marlow Business Quarter</p>
  <div class="contact-line abs" style="left:206px;top:2592px">
    <svg width="15" height="15" viewBox="0 0 24 24" fill="#111"><path d="M6.6 10.8a15 15 0 0 0 6.6 6.6l2.2-2.2c.3-.3.7-.4 1-.2 1.1.4 2.3.6 3.6.6.6 0 1 .4 1 1V20c0 .6-.4 1-1 1A17 17 0 0 1 3 4c0-.6.4-1 1-1h3.5c.6 0 1 .4 1 1 0 1.3.2 2.5.6 3.6.1.3 0 .7-.2 1z"/></svg>
    0700 555 0192
  </div>
  <div class="contact-line abs" style="left:206px;top:2637px">
    <svg width="17" height="14" viewBox="0 0 24 20" fill="#111"><path d="M2 2h20v16H2z"/><path d="M2 3l10 7 10-7" stroke="#fff" stroke-width="2" fill="none"/></svg>
    hello@brindlektr.co.uk
  </div>

  <div class="footer-head abs" style="left:529px;top:2486px">Popular</div>
  <div class="footer-link abs" style="left:526px;top:2528px">Latest Jobs</div>
  <div class="footer-link abs" style="left:526px;top:2563px">How To Find us Maps</div>
  <div class="footer-link abs" style="left:526px;top:2599px">Contact Us</div>

  <a class="footer-contact-btn btn abs">Contact Us</a>
  <div class="follow-box abs">Follow Us <span class="social"></span><span class="social"></span><span class="social"></span></div>
</footer>

<div class="copyright abs">Copyright © 2019 Brindle KTR - All Rights Reserved.</div>

</body>
</html>
```